UPDATE: I have uploaded the selected logo from the other contest, please use it in your designs.

I have a logo design contest as well so not sure how ArtHive handles that. They should integrate at some point. I will describe the overall theme with the logo description. See it for details.

The business card side of it would just build on that same theme.

Target Market(s)

8-40

Industry/Entity Type

Business

Contact Information for Business Card

FirstName LastName
Email

Logo Text

VelMarin

Font styles to use
Sans Serif

Requirements
Must have
• the url VelMarin.com somewhere in it.

```html
<!DOCTYPE html>
<html lang="en">
<head>
<meta charset="utf-8">
<title>VelMarin Business Card</title>
<link rel="stylesheet" href="https://fonts.googleapis.com/css2?family=Jost:wght@200;400&display=swap">
<style>
  :root {
    --card-red: #d14646;
    --cream: #ebe3cf;
  }
  html, body {
    margin: 0;
    padding: 0;
    width: 1200px;
    height: 686px;
    overflow: hidden;
    background: var(--card-red);
  }
  .card {
    position: relative;
    width: 1200px;
    height: 686px;
    background: var(--card-red);
    color: var(--cream);
    font-family: "Jost", sans-serif;
  }
  .brand {
    position: absolute;
    left: 34px;
    top: 40px;
    display: flex;
    align-items: flex-start;
    gap: 18px;
  }
  .brand-name {
    margin: 0;
    font-weight: 200;
    font-size: 150px;
    line-height: 1;
    letter-spacing: 2px;
    text-transform: uppercase;
    color: var(--cream);
  }
  .brand-dot {
    width: 26px;
    height: 26px;
    margin-top: 4px;
    border-radius: 50%;
    background: var(--cream);
  }
  .streaks {
    position: absolute;
    inset: 0;
  }
  .streaks line {
    stroke: var(--cream);
    stroke-width: 3;
    stroke-linecap: round;
  }
  .contact {
    position: absolute;
    left: 43px;
    top: 350px;
    margin: 0;
    font-weight: 400;
    font-style: normal;
  }
  .contact p {
    margin: 0;
    font-size: 52px;
    line-height: 69px;
    letter-spacing: -0.5px;
  }
  .contact .phone {
    font-size: 44px;
    line-height: 72px;
  }
</style>
</head>
<body>
  <main class="card">
    <header class="brand">
      <h1 class="brand-name">VelMarin</h1>
      <span class="brand-dot"></span>
    </header>

    <svg class="streaks" width="1200" height="686" viewBox="0 0 1200 686" aria-hidden="true">
      <line x1="560" y1="214" x2="1200" y2="623"/>
      <line x1="906" y1="333" x2="1200" y2="526"/>
      <line x1="640" y1="397" x2="1046" y2="686"/>
    </svg>

    <address class="contact">
      <p class="name">First Name Last Name</p>
      <p class="email">name@velmarin.com</p>
      <p class="website">www.VelMarin.com</p>
      <p class="phone">Phone 1+(555)-555-5555</p>
    </address>
  </main>
</body>
</html>
```